Business Card design for Accounting and Consulting Firm
R.T. BALLISTER HOLDINGS, LLC
Business Card design for Accounting and Consulting Firm - Financial Services
Creative Brief
Use same font as used in my logo
trajan bold
Professional
Nell Whitcombe
President
I do not want address on the card
nwhitcombe@rtballister-example.com
www.rtballister-example.com
CFO Advisory / Bookkeeping Plinwor Ledgerly Consulting
either logo without text or logo with text whichever is not used on the front of card.
rtballister rtballister
You can use other fonts, I just listed the one that is used in the text with the logo so you would know what that is. Pantone Hex Colors used: BLUE #012377 (C:96 - M:77 - Y:14 - K:4) #021856 (C:96 - M:82 - Y:28 - K:16) #095CD3 (C:95 - M:47 - Y:0 - K:0) Gold #987412 (C:29 - M:37 - Y:91 - K:16) #E4BB2C (C:9 - M:23 - Y:82 - K:1)

```html
<!DOCTYPE html>
<html lang="en">
<head>
<meta charset="utf-8">
<title>R.T. Ballister Holdings — Stationery</title>
<link rel="stylesheet" href="https://fonts.googleapis.com/css2?family=Cinzel:wght@700&family=Open+Sans:wght@400;600&display=swap">
<style>
  :root{
    --blue:#012377;
    --navy:#021856;
    --bright:#095CD3;
    --gold:#987412;
    --gold-light:#E4BB2C;
    --bg:#e6e7e9;
    --paper:#ffffff;
    --ink:#3b3f4a;
    --muted:#8a8f99;
  }
  *{margin:0;padding:0;box-sizing:border-box}
  html,body{width:1200px;height:946px;overflow:hidden;background:var(--bg)}
  body{position:relative;font-family:"Open Sans",Arial,sans-serif;color:var(--ink)}
  .sheet{position:absolute;background:var(--paper);box-shadow:0 2px 6px rgba(0,0,0,.12);overflow:hidden}

  .brand{display:flex;align-items:center;gap:6px}
  .brand-square{width:14px;height:14px;background:var(--gold);flex:none}
  .brand-name{font-family:"Cinzel",Georgia,serif;font-weight:700;color:var(--blue);line-height:1.05;letter-spacing:.02em;white-space:nowrap}
  .brand--light .brand-name{color:#fff}

  .contact{list-style:none;font-size:7px;line-height:10px;color:var(--ink)}
  .contact li{display:flex;align-items:center;gap:4px;white-space:nowrap}
  .contact li::before{content:"";width:4px;height:4px;border-radius:50%;background:var(--blue);flex:none}

  .rule{position:absolute;height:4px}
  .rule--blue{background:linear-gradient(90deg,var(--navy),var(--bright))}
  .rule--gold{background:linear-gradient(90deg,var(--gold),var(--gold-light))}
  .web{position:absolute;font-size:6px;letter-spacing:.15em;color:var(--muted);white-space:nowrap}

  /* letterhead */
  .letterhead{left:243px;top:170px;width:409px;height:548px}
  .letterhead .brand{position:absolute;left:22px;top:18px}
  .letterhead .brand-name{font-size:14px;white-space:normal;width:130px}
  .letterhead .contact{position:absolute;left:205px;top:14px}
  .watermark{position:absolute;left:110px;top:130px;width:300px;height:300px;border-radius:50%;
    background:linear-gradient(180deg,rgba(1,35,119,.12),rgba(228,187,44,.14))}

  /* cards */
  .card{border-radius:6px}
  .card-front{left:673px;top:177px;width:167px;height:115px;background:var(--paper)}
  .card-front .top{position:absolute;inset:0 0 45px 0;background:linear-gradient(180deg,var(--gold-light),var(--gold))}
  .card-front .bottom{position:absolute;left:0;right:0;bottom:0;height:78px;background:linear-gradient(180deg,var(--blue),var(--navy))}
  .card-front .brand{position:absolute;left:18px;top:52px}
  .card-front .brand-name{font-size:11px}
  .tagline{position:absolute;left:0;right:0;bottom:8px;text-align:center;font-size:5px;letter-spacing:.12em;color:var(--gold-light)}

  .card-back-dark{left:673px;top:308px;width:167px;height:115px;background:linear-gradient(180deg,var(--gold),var(--gold-light))}
  .card-back-dark .panel{position:absolute;left:0;right:0;top:0;height:78px;background:linear-gradient(180deg,var(--blue),var(--navy))}
  .card-back-dark .brand{position:absolute;left:18px;top:26px}
  .card-back-dark .brand-name{font-size:11px}

  .card-info{left:861px;top:177px;width:178px;height:110px}
  .card-info .brand{position:absolute;left:10px;top:10px}
  .card-info .brand-name{font-size:8px}
  .card-info .person{position:absolute;left:72px;top:34px}
  .person .name{font-size:7px;font-weight:600;color:var(--gold)}
  .person .title{font-size:6px;color:var(--muted);margin-bottom:5px}
  .card-info .contact{font-size:5.5px;line-height:8px}

  .card-plain{left:861px;top:308px;width:178px;height:110px}
  .card-plain .brand{position:absolute;left:14px;top:20px}
  .card-plain .brand-name{font-size:8px}
  .card-plain .contact{position:absolute;left:34px;top:46px;font-size:5.5px;line-height:8px}

  /* envelope */
  .envelope{left:673px;top:449px;width:366px;height:203px}
  .envelope .brand{position:absolute;left:18px;top:18px}
  .envelope .brand-name{font-size:11px}
  .envelope .contact{position:absolute;left:32px;top:58px;font-size:6px;line-height:9px}
  .window{position:absolute;left:238px;top:92px;width:102px;height:50px;border:1px solid #c9ccd4;border-radius:4px;background:#f3f4f8}
</style>
</head>
<body>

<section class="sheet letterhead" aria-label="Letterhead">
  <div class="watermark"></div>
  <div class="brand"><span class="brand-square"></span><span class="brand-name">R.T. BALLISTER HOLDINGS, LLC</span></div>
  <ul class="contact">
    <li>(555) 014-2201</li>
    <li>(555) 014-2202</li>
    <li>nwhitcombe@rtballister-example.com</li>
    <li>www.rtballister-example.com</li>
  </ul>
  <span class="web" style="left:170px;bottom:30px">www.rtballister-example.com</span>
  <div class="rule rule--blue" style="left:10px;bottom:18px;width:180px"></div>
  <div class="rule rule--gold" style="left:200px;bottom:18px;width:199px"></div>
</section>

<section class="sheet card card-front" aria-label="Business card front">
  <div class="top"></div>
  <div class="bottom"></div>
  <div class="brand brand--light"><span class="brand-square"></span><span class="brand-name">R.T. BALLISTER</span></div>
  <p class="tagline">CFO ADVISORY / BOOKKEEPING</p>
</section>

<section class="sheet card card-back-dark" aria-label="Business card alternate front">
  <div class="panel"></div>
  <div class="brand brand--light"><span class="brand-square"></span><span class="brand-name">R.T. BALLISTER</span></div>
</section>

<section class="sheet card card-info" aria-label="Business card back">
  <div class="brand"><span class="brand-square"></span><span class="brand-name">R.T. BALLISTER</span></div>
  <div class="person">
    <p class="name">Nell Whitcombe</p>
    <p class="title">President</p>
    <ul class="contact">
      <li>(555) 014-2201</li>
      <li>(555) 014-2203</li>
      <li>nwhitcombe@rtballister-example.com</li>
      <li>www.rtballister-example.com</li>
    </ul>
  </div>
  <div class="rule rule--blue" style="left:0;bottom:0;width:89px;height:3px"></div>
  <div class="rule rule--gold" style="left:89px;bottom:0;width:89px;height:3px"></div>
</section>

<section class="sheet card card-plain" aria-label="Compliment card">
  <div class="brand"><span class="brand-square"></span><span class="brand-name">R.T. BALLISTER</span></div>
  <ul class="contact">
    <li>(555) 014-2201</li>
    <li>(555) 014-2202</li>
    <li>www.rtballister-example.com</li>
  </ul>
  <div class="rule rule--blue" style="left:0;bottom:0;width:89px;height:3px"></div>
  <div class="rule rule--gold" style="left:89px;bottom:0;width:89px;height:3px"></div>
</section>

<section class="sheet envelope" aria-label="Envelope">
  <div class="brand"><span class="brand-square"></span><span class="brand-name">R.T. BALLISTER</span></div>
  <ul class="contact">
    <li>(555) 014-2201</li>
    <li>(555) 014-2202</li>
    <li>nwhitcombe@rtballister-example.com</li>
    <li>www.rtballister-example.com</li>
  </ul>
  <div class="window"></div>
  <span class="web" style="left:20px;bottom:22px">www.rtballister-example.com</span>
  <div class="rule rule--blue" style="left:0;bottom:10px;width:170px"></div>
  <div class="rule rule--gold" style="left:180px;bottom:10px;width:186px"></div>
</section>

</body>
</html>
```